Web design for online activity booking website

Our activity booking website uTrundle.net is looking outdated and needing a loving revamp on its design and STRUCTURE. it was initially created as a destination guide before we modified the homepage slightly to sell activities. So please DON'T RELY on the current website for your design. Now, the focus is ACTIVITY, while guide/ info should come only as secondary.

In other words, we will be doing something very similar to Wandelo.com (a bit crowded for our liking) and FindMyOuting.com. If you could capture the best essences of both, that would be awesome! Besides, we also like roostly.com's simplicity.

SIMPLE, CLEAN, BRIGHT, USER and MOBILE FRIENDLY please :)

We have a new logo created and some wireframes (a few more in progress) so you know the basic components required in each page. These are just rough ideas so please ignore the ratio/size, colours etc and if you have a better way of arranging or simplifying things, please do so :)

Help us make it a website that everyone would love!

Thank you in advance for your time and artistry.

Target Market(s)

Internet savvy travellers between 18-65

Industry/Entity Type

Tourism

Number of Pages Required

5+ page

Requirements
Must have
• SIMPLE, CLEAN feel, USER and MOBILE FRIENDLY please :)
• See attachments for rough structure. Will also need standard pages such as:
• - About Us
• - Contact Us
• - Wishlist etc
• Message from our developer "designer to keep layers in PSD format accurately so html/css code does not need to lead a mess in photoshop"
Nice to have
• UPDATE: We are so thrilled to receive so many web designs but on the other hand, the submissions are getting too generic and everyone's designs is almost looking identical (many look like they are “borrowed” from existing popular websites). This is making the selection and decision process very difficult.
• So instead of sending us more of the very similar homepage design with minor tweaks (which we can do during handover section anyway), please send us a design of more specific page of our website. Please refer job brief, file no. 5 - Product detail page.
• This will give us better idea of your skills and choose the best as winner to work on the rest of our web pages.
Should not have
• No dark background please

```html
<!DOCTYPE html>
<html lang="en">
<head>
<meta charset="utf-8">
<title>uTrundle.net – Book Activities</title>
<link href="https://fonts.googleapis.com/css2?family=Mulish:wght@300;400;600;700;800&display=swap" rel="stylesheet">
<style>
:root{
  --purple:#6b2c8f;
  --purple-dark:#55206f;
  --orange:#f07b3f;
  --pink:#e6197f;
  --grey-bg:#eeeeee;
  --white:#ffffff;
  --text:#3d3d3d;
  --muted:#777777;
  --line:#cfcfcf;
  --footer:#e4e4e4;
}
*{box-sizing:border-box;margin:0;padding:0}
html,body{width:1200px;height:3495px;overflow:hidden}
body{font-family:"Mulish",sans-serif;color:var(--text);background:var(--white);position:relative}
a{color:inherit;text-decoration:none}

/* Hero */
.hero{position:absolute;left:0;top:0;width:1200px;height:620px;overflow:hidden}
.hero-photo{position:absolute;inset:0;background:
  radial-gradient(ellipse at 55% 35%,#f3e2b8 0%,#c8a76e 25%,#7d6a4c 55%,#3d3528 100%)}
.hero-photo::after{content:"";position:absolute;left:0;right:0;bottom:0;height:260px;background:linear-gradient(180deg,rgba(40,34,26,0) 0%,#2b251d 100%)}
.top-bar{position:absolute;left:0;top:0;width:100%;height:6px;background:var(--purple)}
.logo{position:absolute;left:88px;top:6px;width:194px;height:60px;background:var(--purple);display:flex;align-items:center;justify-content:center;color:var(--white);font-weight:800;font-size:30px;letter-spacing:-.5px}
.top-nav{position:absolute;right:84px;top:32px;display:flex;gap:36px;color:var(--white);font-size:12.5px;font-weight:700;text-transform:uppercase}
.top-nav span{display:flex;align-items:center;gap:6px}
.hero-arrow{position:absolute;top:278px;width:36px;height:36px;border-radius:50%;background:rgba(255,255,255,.35);display:flex;align-items:center;justify-content:center}
.hero-arrow.prev{left:52px}.hero-arrow.next{right:50px}
.hero-title{position:absolute;left:0;right:0;top:248px;text-align:center;color:var(--white);font-weight:800;font-size:50px;letter-spacing:1px}
.hero-sub{position:absolute;left:0;right:0;top:318px;text-align:center;color:var(--white);font-weight:700;font-size:26px;letter-spacing:1px}
.search{position:absolute;left:280px;top:444px;width:640px;height:70px;background:rgba(255,255,255,.35);display:flex;align-items:center;padding:0 12px;gap:14px}
.search .select{height:48px;background:var(--white);display:flex;align-items:center;justify-content:space-between;padding:0 16px;font-size:15px;color:var(--text)}
.search .where{width:230px}.search .what{width:228px}
.search .go{width:124px;height:48px;background:var(--purple);color:var(--white);font-weight:700;font-size:15px;display:flex;align-items:center;justify-content:center;margin-left:10px}

/* Section titles */
.section{position:absolute;left:0;width:1200px}
.section-title{position:absolute;left:0;right:0;text-align:center;font-size:29px;font-weight:600;letter-spacing:1px;color:#333}
.section-title em{font-style:normal;color:var(--purple)}
.title-rule{position:absolute;left:50%;transform:translateX(-50%);width:200px;height:2px;background:var(--line)}
.title-mark{position:absolute;left:50%;transform:translateX(-50%);width:44px;height:10px;background:var(--orange);border-radius:2px}

.destinations{top:620px;height:794px;background:var(--grey-bg)}
.activities{top:1414px;height:816px;background:var(--white)}
.inspirations{top:2230px;height:632px;background:var(--grey-bg)}
.seo{top:2862px;height:353px;background:var(--white)}

/* Tiles */
.tile{position:absolute;width:327px;height:250px;overflow:hidden}
.tile .photo{position:absolute;inset:0}
.tile .caption{position:absolute;left:0;right:0;bottom:0;height:48px;background:rgba(0,0,0,.45);color:var(--white);display:flex;align-items:center;justify-content:space-between;padding:0 14px;font-size:18px}
.tile .caption b{font-weight:800}
.col1{left:88px}.col2{left:436px}.col3{left:783px}
.carousel-arrow{position:absolute;width:44px;height:44px;border-radius:50%;background:var(--white);box-shadow:0 1px 4px rgba(0,0,0,.25);display:flex;align-items:center;justify-content:center}
.btn-more{position:absolute;height:52px;background:var(--purple);color:var(--white);font-size:16px;font-weight:600;display:flex;align-items:center;justify-content:center;border-radius:2px}

.act-caption{position:absolute;left:0;right:0;bottom:0;height:62px;background:linear-gradient(180deg,rgba(0,0,0,0),rgba(0,0,0,.6));color:var(--white);padding:16px 18px 0;font-size:14px;line-height:18px}
.feature{background:#3b3b3d;color:var(--white);padding:22px 28px}
.feature h3{font-size:22px;font-weight:600}
.feature .stars{margin-top:6px;font-size:12px;color:#ddd;display:flex;align-items:center;gap:6px}
.feature p{margin-top:8px;font-size:11px;line-height:14px;color:#d8d8d8}
.feature .price-label{position:absolute;left:28px;top:188px;font-size:13px}
.feature .price{position:absolute;left:28px;top:202px;font-size:30px;font-weight:600}
.feature .book{position:absolute;right:26px;top:190px;width:98px;height:34px;background:var(--pink);font-size:12px;font-weight:700;display:flex;align-items:center;justify-content:center}

/* Inspirations */
.big-post{position:absolute;left:93px;top:133px;width:469px}
.big-post .photo{height:242px;position:relative}
.play{position:absolute;left:50%;top:50%;transform:translate(-50%,-50%)}
.big-post h4{margin-top:28px;font-size:17px;font-weight:600;color:#333}
.meta{font-size:12.5px;color:var(--muted);margin-top:10px}
.big-post p{margin-top:14px;font-size:13px;line-height:19px;color:#888}
.show-more{display:inline-block;margin-top:18px;font-size:15px;color:var(--purple);text-decoration:underline;font-weight:600}
.mini-post{position:absolute;left:602px;width:520px;height:121px;border-bottom:1px solid var(--line)}
.mini-post .photo{position:absolute;left:0;top:0;width:186px;height:121px}
.mini-post .body{position:absolute;left:200px;top:4px;width:320px}
.mini-post h5{font-size:17px;font-weight:600;color:#333}
.mini-post p{margin-top:8px;font-size:12.5px;line-height:17px;color:#888}
.mini-post .meta{margin-top:12px;font-size:12px;color:#555}

/* SEO */
.seo-col{position:absolute;top:140px;list-style:none}
.seo-col li{font-size:14.5px;height:28.7px;display:flex;align-items:center;gap:8px;color:#444}
.seo-col li::before{content:"";border-left:5px solid #555;border-top:4px solid transparent;border-bottom:4px solid transparent}
.seo-col li.active{color:var(--purple)}
.seo-col li.active::before{border-left-color:var(--purple)}

/* Footer */
.footer{position:absolute;left:0;top:3215px;width:1200px;height:234px;background:var(--footer)}
.f-col{position:absolute;top:42px}
.f-col h6{font-size:16px;font-weight:600;color:#444;letter-spacing:.5px;margin-bottom:10px}
.f-col li{list-style:none;font-size:12.5px;color:#555;height:21px}
.newsletter p{font-size:12.5px;color:#555}
.news-form{display:flex;margin-top:12px}
.news-form .input{width:166px;height:34px;background:var(--white);border:1px solid var(--line);font-size:12px;color:#aaa;padding:9px 10px}
.news-form .sub{width:102px;height:34px;background:var(--purple);color:var(--white);font-size:12px;font-weight:700;display:flex;align-items:center;justify-content:center;margin-left:6px}
.social{display:flex;gap:14px;margin-top:6px}
.social span{width:34px;height:34px;border-radius:50%;background:var(--purple)}
.bottom-bar{position:absolute;left:0;top:3449px;width:1200px;height:46px;background:var(--purple);color:var(--white);font-size:12.5px;display:flex;align-items:center;justify-content:center}
.bottom-bar .tag{position:absolute;right:22px}
</style>
</head>
<body>

<header class="hero">
  <div class="hero-photo" role="img" aria-label="Couple taking a selfie on a rocky summit above the sea at sunset"></div>
  <div class="top-bar"></div>
  <a class="logo" href="#">uTrundle</a>
  <nav class="top-nav">
    <span><svg width="13" height="12" viewBox="0 0 13 12"><path d="M6.5 11 1.5 6a3 3 0 0 1 5-3.5A3 3 0 0 1 11.5 6z" fill="#fff"/></svg>Wishlist</span>
    <span><svg width="14" height="12" viewBox="0 0 14 12"><path d="M0 1h2.5l2 7h7l2-5H4" stroke="#fff" stroke-width="1.6" fill="none"/><circle cx="5" cy="10.5" r="1.2" fill="#fff"/><circle cx="11" cy="10.5" r="1.2" fill="#fff"/></svg>Cart</span>
    <span><svg width="12" height="12" viewBox="0 0 12 12"><circle cx="6" cy="6" r="5.5" fill="#fff"/></svg>EN</span>
    <span>(€) Euro</span>
    <span><svg width="12" height="12" viewBox="0 0 12 12"><circle cx="6" cy="6" r="5.5" fill="#fff"/></svg>Help</span>
    <span><svg width="12" height="12" viewBox="0 0 12 12"><circle cx="6" cy="3.5" r="3" fill="#fff"/><path d="M0 12a6 5 0 0 1 12 0z" fill="#fff"/></svg>Log in</span>
  </nav>
  <div class="hero-arrow prev"><svg width="12" height="14" viewBox="0 0 12 14"><path d="M9 1 3 7l6 6" stroke="#fff" stroke-width="2.5" fill="none"/></svg></div>
  <div class="hero-arrow next"><svg width="12" height="14" viewBox="0 0 12 14"><path d="M3 1l6 6-6 6" stroke="#fff" stroke-width="2.5" fill="none"/></svg></div>
  <h1 class="hero-title">BOOK ACTIVITIES</h1>
  <p class="hero-sub">YOUR ADVENTURE STARTS HERE!</p>
  <form class="search">
    <div class="select where">Where to, my friend? <svg width="10" height="6"><path d="M0 0h10L5 6z" fill="#333"/></svg></div>
    <div class="select what">Choose an activity <svg width="10" height="6"><path d="M0 0h10L5 6z" fill="#333"/></svg></div>
    <div class="go">LET'S GO!</div>
  </form>
</header>

<section class="section destinations">
  <h2 class="section-title" style="top:40px">MOST POPULAR <em>DESTINATIONS</em></h2>
  <div class="title-rule" style="top:91px"></div>
  <div class="title-mark" style="top:82px" role="img" aria-label="Small orange heading ornament"></div>

  <div class="tile col1" style="top:130px"><div class="photo" role="img" aria-label="Group cheering on a boat trip" style="background:linear-gradient(160deg,#7a8fa8,#b84036 55%,#4e2a26)"></div><div class="caption"><span>Tenerife</span><b>43 activities</b></div></div>
  <div class="tile col2" style="top:130px"><div class="photo" role="img" aria-label="Helicopter over autumn woodland" style="background:linear-gradient(180deg,#8fb1cc,#c7b48a 55%,#7a5a2c)"></div><div class="caption"><span>Lanzarote</span><b>43 activities</b></div></div>
  <div class="tile col3" style="top:130px"><div class="photo" role="img" aria-label="Quad bikes on a dusty desert track" style="background:linear-gradient(180deg,#b8a58a,#8e6b48 60%,#5c4330)"></div><div class="caption"><span>Fuerteventura</span><b>43 activities</b></div></div>
  <div class="tile col1" style="top:408px"><div class="photo" role="img" aria-label="Tropical garden with palm trees" style="background:linear-gradient(180deg,#5f6b55,#3c4733 60%,#2b3225)"></div><div class="caption"><span>El Hierro</span><b>43 activities</b></div></div>
  <div class="tile col2" style="top:408px"><div class="photo" role="img" aria-label="Historic building with palm trees under blue sky" style="background:linear-gradient(180deg,#5d8ed0,#b9c4c8 55%,#6c6a55)"></div><div class="caption"><span>La Palma</span><b>43 activities</b></div></div>
  <div class="tile col3" style="top:408px"><div class="photo" role="img" aria-label="Caver exploring a red rock cave" style="background:linear-gradient(160deg,#7d3b2c,#a86248 50%,#3e231b)"></div><div class="caption"><span>Porta Santo</span><b>43 activities</b></div></div>

  <div class="carousel-arrow" style="left:74px;top:374px"><svg width="12" height="16" viewBox="0 0 12 16"><path d="M9 2 3 8l6 6" stroke="#333" stroke-width="3" fill="none"/></svg></div>
  <div class="carousel-arrow" style="left:1080px;top:374px"><svg width="12" height="16" viewBox="0 0 12 16"><path d="M3 2l6 6-6 6" stroke="#333" stroke-width="3" fill="none"/></svg></div>

  <a class="btn-more" href="#" style="left:471px;top:692px;width:261px">More Popular Destinations »</a>
</section>

<section class="section activities">
  <h2 class="section-title" style="top:40px">MOST POPULAR <em>ACTIVITIES</em></h2>
  <div class="title-rule" style="top:91px"></div>
  <div class="title-mark" style="top:82px" role="img" aria-label="Small orange heading ornament"></div>

  <div class="tile col1" style="top:136px;height:251px"><div class="photo" role="img" aria-label="Cyclist riding below a volcano" style="background:linear-gradient(180deg,#8fb0d6,#c7d3dc 40%,#8a7258 70%,#5a4a3a)"></div><div class="act-caption">Biking in Teide 3h<br>TENERIFE</div></div>
  <div class="tile col2 feature" style="top:136px;height:251px">
    <h3>Biking in Teide 3h</h3>
    <div class="stars"><svg width="68" height="11" viewBox="0 0 68 11"><g fill="#fff"><path id="s" d="M5.5 0l1.6 3.6 3.9.4-2.9 2.6.8 3.9L5.5 8.5 2.1 10.5l.8-3.9L0 4l3.9-.4z"/><use href="#s" x="14"/><use href="#s" x="28"/><use href="#s" x="42"/><use href="#s" x="56"/></g></svg>196 Reviews</div>
    <p>Lorem Ipsum has been the industry's standard dummy text ever since the 1500s, when an unknown printer took a galley of type and scrambled it to make a type specimen book. It has survived not only five centuries, but also the leap into electronic typesetting.</p>
    <div class="price-label">Price from:</div>
    <div class="price">$100</div>
    <div class="book">BOOK NOW</div>
  </div>
  <div class="tile col3" style="top:136px;height:251px"><div class="photo" role="img" aria-label="Dolphin swimming in blue water" style="background:linear-gradient(180deg,#1f6fb8,#134f8d 60%,#0c3766)"></div><div class="act-caption">Biking in Teide 3h<br>TENERIFE</div></div>
  <div class="tile col1" style="top:413px;height:251px"><div class="photo" role="img" aria-label="Turquoise bay with boats" style="background:linear-gradient(180deg,#bcd8ea,#37b4d2 35%,#1d8fb8 70%,#4a7fa0)"></div><div class="act-caption">Biking in Teide 3h<br>TENERIFE</div></div>
  <div class="tile col2" style="top:413px;height:251px"><div class="photo" role="img" aria-label="Hikers on a coastal cliff path" style="background:linear-gradient(160deg,#9fbad2,#b58a5d 40%,#7a5c3e 70%,#3f8a8f)"></div><div class="act-caption">Biking in Teide 3h<br>TENERIFE</div></div>
  <div class="tile col3" style="top:413px;height:251px"><div class="photo" role="img" aria-label="Riders on an inflatable towed boat" style="background:linear-gradient(180deg,#2a5b8c,#1d4772 50%,#e3c532 75%,#d8b21f)"></div><div class="act-caption">Biking in Teide 3h<br>TENERIFE</div></div>

  <div class="carousel-arrow" style="left:74px;top:377px"><svg width="12" height="16" viewBox="0 0 12 16"><path d="M9 2 3 8l6 6" stroke="#333" stroke-width="3" fill="none"/></svg></div>
  <div class="carousel-arrow" style="left:1080px;top:377px"><svg width="12" height="16" viewBox="0 0 12 16"><path d="M3 2l6 6-6 6" stroke="#333" stroke-width="3" fill="none"/></svg></div>

  <a class="btn-more" href="#" style="left:470px;top:702px;width:260px">More Popular Activities »</a>
</section>

<section class="section inspirations">
  <h2 class="section-title" style="top:40px">TRAVEL <em>INSPIRATIONS</em></h2>
  <div class="title-rule" style="top:91px"></div>
  <div class="title-mark" style="top:82px" role="img" aria-label="Small orange heading ornament"></div>

  <article class="big-post">
    <div class="photo" role="img" aria-label="Close-up of a pale flower on dark rocks" style="background:radial-gradient(ellipse at 45% 45%,#c9b2a8,#6a5448 45%,#2a211c)">
      <svg class="play" width="64" height="64" viewBox="0 0 64 64"><circle cx="32" cy="32" r="31" fill="rgba(0,0,0,.45)"/><path d="M25 19l21 13-21 13z" fill="#fff"/></svg>
    </div>
    <h4>Nemo enim ipsam voluptatem quia voluptas sit aspernatur</h4>
    <div class="meta">April 23 2015 &nbsp; / &nbsp; 2 comments &nbsp; / &nbsp; 6 hours ago</div>
    <p>Lorem ipsum dolor sit amet, consectetur adipiscing elit, sed do eiusmod tempor incididunt ut labore et dolore magna aliqua. Ut enim ad minim veniam, quis nostrud exercitation ullamco laboris nisi ut aliquip ex ea commodo consequat. Duis aute irure dolor in reprehenderit in voluptate</p>
    <a class="show-more" href="#">SHOW MORE &gt;&gt;</a>
  </article>

  <article class="mini-post" style="top:133px">
    <div class="photo" role="img" aria-label="Hiker on a dark mountain ridge" style="background:linear-gradient(160deg,#8a8c8e,#4b4742 60%,#2a2826)"><svg class="play" width="40" height="40" viewBox="0 0 40 40"><circle cx="20" cy="20" r="19" fill="rgba(0,0,0,.45)"/><path d="M15 11l14 9-14 9z" fill="#fff"/></svg></div>
    <div class="body"><h5>Nemo enim ipsam voluptatem quia</h5><p>Lorem ipsum dolor sit amet, consectetur adipiscing elit, sed do eiusmod tempor incididunt ut labore et dolore magna aliqua. Ut enim ad minim veniam,</p><div class="meta">3 minutes ago &nbsp; / &nbsp; 0 comments</div></div>
  </article>
  <article class="mini-post" style="top:282px">
    <div class="photo" role="img" aria-label="Kitesurfer over the sea" style="background:linear-gradient(180deg,#c8d6e2,#8ea8bd 55%,#2f5878)"><svg class="play" width="40" height="40" viewBox="0 0 40 40"><circle cx="20" cy="20" r="19" fill="rgba(0,0,0,.45)"/><path d="M15 11l14 9-14 9z" fill="#fff"/></svg></div>
    <div class="body"><h5>Nemo enim ipsam voluptatem quia</h5><p>Lorem ipsum dolor sit amet, consectetur adipiscing elit, sed do eiusmod tempor incididunt ut labore et dolore magna aliqua. Ut enim ad minim veniam,</p><div class="meta">3 minutes ago &nbsp; / &nbsp; 0 comments</div></div>
  </article>
  <article class="mini-post" style="top:438px">
    <div class="photo" role="img" aria-label="Travellers relaxing at a table" style="background:linear-gradient(160deg,#8d9a78,#5a6b86 55%,#3c3f52)"><svg class="play" width="40" height="40" viewBox="0 0 40 40"><circle cx="20" cy="20" r="19" fill="rgba(0,0,0,.45)"/><path d="M15 11l14 9-14 9z" fill="#fff"/></svg></div>
    <div class="body"><h5>Nemo enim ipsam voluptatem quia</h5><p>Lorem ipsum dolor sit amet, consectetur adipiscing elit, sed do eiusmod tempor incididunt ut labore et dolore magna aliqua. Ut enim ad minim veniam,</p><div class="meta">3 minutes ago &nbsp; / &nbsp; 0 comments</div></div>
  </article>
</section>

<section class="section seo">
  <h2 class="section-title" style="top:40px">USEFUL FOR <em>SEO</em></h2>
  <div class="title-rule" style="top:91px"></div>
  <div class="title-mark" style="top:82px" role="img" aria-label="Small orange heading ornament"></div>
  <ul class="seo-col" style="left:88px">
    <li class="active">Top things to do in Tenerife!</li><li>Top things to do in Barcelona</li><li>Top things to do in Paris!</li><li>Top things to do in London!</li><li>Top things to do in Berlin!</li><li>Top things to do in Kuala Lumpur!</li>
  </ul>
  <ul class="seo-col" style="left:356px">
    <li>Top things to do in Barcelona!</li><li>Top things to do in Barcelona!</li><li>Top things to do in Barcelona!</li><li>Top things to do in Barcelona!</li><li>Top things to do in Barcelona!</li><li>Top things to do in Barcelona!</li>
  </ul>
  <ul class="seo-col" style="left:622px">
    <li>Top things to do in Tenerife!</li><li>Top things to do in Barcelona</li><li>Top things to do in Paris!</li><li>Top things to do in London!</li><li>Top things to do in Berlin!</li><li>Top things to do in Paris!</li>
  </ul>
  <ul class="seo-col" style="left:885px">
    <li>Top things to do in Barcelona!</li><li>Top things to do in Barcelona!</li><li>Top things to do in Barcelona!</li><li>Top things to do in Barcelona!</li><li>Top things to do in Barcelona!</li><li>Top things to do in Barcelona!</li>
  </ul>
</section>

<footer class="footer">
  <div class="f-col" style="left:86px"><h6>COMPANY</h6><ul><li>About uTrundle.net</li><li>Corporate Info</li><li>Site map?</li><li>Blog</li><li>Careers</li></ul></div>
  <div class="f-col" style="left:354px"><h6>SUPPORT</h6><ul><li>Contact us</li><li>FAQs</li><li>Legal</li><li>Privacy Policy</li><li>Legal</li></ul></div>
  <div class="f-col" style="left:587px"><h6>PARTNERSHIPS</h6><ul><li>Supplier sign-up</li><li>Affiliate Programs</li></ul><h6 style="margin-top:12px">LOGIN</h6><ul><li>Customers</li><li>Suppliers</li></ul></div>
  <div class="f-col newsletter" style="left:834px"><h6>NEWSLETTERS</h6><p>For travel inspiration, news and discounts!</p>
    <div class="news-form"><div class="input">Your email</div><div class="sub">SUBSCRIBE</div></div>
    <h6 style="margin-top:16px">BE SOCIAL</h6>
    <div class="social"><span></span><span></span><span></span><span></span><span></span><span></span></div>
  </div>
</footer>
<div class="bottom-bar">Copyright © 2015. All Rights Reserved<span class="tag">C6</span></div>

</body>
</html>
```